Admin Backend Redesign

We need a redesign for our backend which supoosed to make the backoffice look more modern!

I will add screenshots of the backoffice so you know what data will be shown in the Admin.

Have in mind that the users of this backend are Doctors. We need a clinical look, modern and sharp. The backoffice is responsive, have that in mind. We need the backoffice to look as professional as possible.

The theme used for the website is: http://velmora.quillstack-sample.com/

ON the main page of the backoffice, under every widget i need some space to write an explanation what the widget is about.

The color code used in our logo and website is #57aad4 combined with white.

We are open for ideas!
Updates

Project Deadline Extended
Reason: Designs are ok, but nothing innovative. Please use more modern designs!

Project Deadline Extended
Reason: Havent recieved a perfect design yet. Please read instructions carefully! Thank you

Project Deadline Extended
Reason: Hey everybody, sorry for the delay. We will decide in 3 days. If anyone wants to add a Design, that would be great.

Target Market(s)

Doctors, therapists

Industry/Entity Type

It Professional

Font styles to use
Sans Serif

Requirements
Must have
• Must look uptodate, modern, like new back offices look nowadays

```html
<!DOCTYPE html>
<html lang="de">
<head>
<meta charset="utf-8">
<title>Admin Site – Dashboard</title>
<link rel="stylesheet" href="https://fonts.googleapis.com/css2?family=Arimo:wght@400;700&display=swap">
<style>
:root{
  --topbar:#1b1b1b;
  --sidebar:#6a6a6a;
  --sidebar-item:#5e5e5e;
  --sidebar-line:#4a4a4a;
  --accent:#2f8fc4;
  --accent-light:#57aad4;
  --canvas:#e4e4e4;
  --panel:#ffffff;
  --panel-head:#e6e6e6;
  --border:#c9c9c9;
  --text:#1d1d1d;
  --muted:#444;
  --footer:#2a2a2a;
}
*{box-sizing:border-box;margin:0;padding:0}
html,body{width:1200px;height:1000px;overflow:hidden}
body{font-family:"Arimo",Arial,sans-serif;color:var(--text);background:#fff;position:relative}
.topbar{position:absolute;left:0;top:0;width:1200px;height:42px;background:linear-gradient(#2c2c2c,#111);color:#fff}
.brand{position:absolute;left:57px;top:9px;font-size:21px;font-weight:700}
.topnav{position:absolute;left:222px;top:0;height:42px;display:flex;border-left:1px solid #3a3a3a}
.topnav a{color:#fff;text-decoration:none;font-size:14px;display:flex;align-items:center;gap:8px;padding:0 27px 0 24px;border-right:1px solid #3a3a3a}
.top-icons{position:absolute;right:105px;top:6px;display:flex;gap:30px}
.top-icon{position:relative;width:30px;height:30px}
.badge{position:absolute;right:-4px;top:-1px;background:var(--accent-light);color:#fff;font-size:9px;border-radius:6px;padding:1px 3px}
.sidebar{position:absolute;left:0;top:42px;width:222px;height:880px;background:var(--sidebar)}
.user{height:134px;border-bottom:2px solid var(--sidebar-line);position:relative;background:#777}
.avatar{position:absolute;left:31px;top:20px;width:70px;height:70px;border-radius:50%;background:#fff;overflow:hidden}
.welcome{position:absolute;left:103px;top:27px;color:#fff;font-size:15px;text-align:center;line-height:22px}
.welcome b{display:block;font-size:16px}
.logout{position:absolute;left:114px;top:90px;width:71px;height:24px;border:1px solid #888;border-radius:3px;background:linear-gradient(#f4f4f4,#cfcfcf);font-size:14px;font-weight:700;color:#222;text-align:center;line-height:22px}
.menu{position:absolute;top:166px;left:0;width:222px}
.menu li{list-style:none;height:34px;display:flex;align-items:center;gap:9px;padding-left:31px;color:#fff;font-size:16px;background:linear-gradient(#6d6d6d,#575757);border-bottom:1px solid var(--sidebar-line)}
.menu li.active{background:linear-gradient(#45a7da,#1f82bd);width:236px;clip-path:polygon(0 0,222px 0,236px 50%,222px 100%,0 100%)}
.main{position:absolute;left:222px;top:42px;width:978px;height:880px;background:var(--canvas)}
.page-head{height:72px;background:linear-gradient(#f2f2f2,#d9d9d9);border-bottom:1px solid #c4c4c4;display:flex;align-items:center;padding-left:28px;gap:14px}
.page-head h1{font-size:21px;font-weight:700}
.crumbs{position:absolute;left:25px;top:83px;width:910px;height:36px;background:linear-gradient(#fff,#e3e3e3);border:1px solid #c9c9c9;border-radius:4px;box-shadow:0 2px 3px rgba(0,0,0,.15);display:flex;align-items:center;font-size:14px}
.crumb-home{height:34px;width:115px;background:linear-gradient(#4aaadc,#1d7fb9);color:#fff;display:flex;align-items:center;gap:6px;padding-left:24px;clip-path:polygon(0 0,100px 0,115px 50%,100px 100%,0 100%);border-radius:4px 0 0 4px}
.crumb-current{margin-left:12px}
.panel{position:absolute;background:var(--panel);border:1px solid var(--border);box-shadow:0 1px 2px rgba(0,0,0,.1)}
.panel-head{height:31px;background:linear-gradient(#f3f3f3,#dedede);border-bottom:1px solid var(--border);display:flex;align-items:center;justify-content:space-between;padding:0 14px 0 15px;font-size:12px}
.panel-head.large{font-size:16px;height:35px;padding-left:12px}
.tile-title{position:absolute;right:23px;text-align:right}
.tile-title strong{display:block;font-size:21px;font-weight:400;margin-bottom:6px}
.tile-title span{font-size:13px}
.welcome-body{padding:14px 24px;font-size:12px;line-height:15px}
.status{display:flex;align-items:center;gap:17px;margin-bottom:12px}
.btn{background:linear-gradient(#4aaadc,#1f7fba);color:#fff;border-radius:3px;font-weight:700;border:1px solid #1a6fa3}
.btn-ok{font-size:14px;padding:5px 16px}
.legend{position:absolute;left:307px;top:58px;font-size:12px;color:#444;list-style:none}
.legend li{display:flex;align-items:center;gap:6px;height:15.4px}
.legend i{width:16px;height:11px;display:block}
.search{position:absolute;right:22px;top:44px;display:flex}
.search div{width:176px;height:26px;border:1px solid #bbb;border-radius:3px 0 0 3px;font-size:13px;color:#999;padding:5px 11px}
.search span{width:45px;height:26px;background:linear-gradient(#4aaadc,#1f7fba);border-radius:0 3px 3px 0;display:flex;align-items:center;justify-content:center}
.stat-table{position:absolute;left:22px;top:88px;width:380px;border-collapse:collapse;font-size:14px}
.stat-table th{text-align:left;font-weight:700;height:18px;border-bottom:1px solid #aaa}
.stat-table td{height:22px;border-bottom:1px solid #aaa}
.stat-table td:nth-child(3),.stat-table th:nth-child(3){text-align:center}
.pager-info{position:absolute;left:22px;top:232px;font-size:14px}
.pager{position:absolute;right:22px;top:226px;display:flex;gap:4px;font-size:12px}
.pager .btn{height:26px;display:flex;align-items:center;padding:0 7px;font-weight:400}
.footer{position:absolute;left:0;top:922px;width:1200px;height:43px;background:var(--footer);color:#bbb;font-size:13px;padding:14px 0 0 32px}
</style>
</head>
<body>
<header class="topbar">
  <div class="brand">Admin Site</div>
  <nav class="topnav">
    <a href="#"><svg width="18" height="16" viewBox="0 0 18 16"><path d="M9 1 1 8h2.5v7h4v-4h3v4h4V8H17z" fill="#fff"/></svg>Home</a>
    <a href="#">Dropdown <svg width="12" height="8" viewBox="0 0 12 8"><path d="M0 0h12L6 8z" fill="#fff"/></svg></a>
  </nav>
  <div class="top-icons">
    <div class="top-icon"><svg width="30" height="30" viewBox="0 0 30 30"><rect x="1" y="8" width="27" height="19" fill="#fff"/><path d="M1 8l13.5 11L28 8" fill="none" stroke="#333" stroke-width="1.5"/></svg><span class="badge">9</span></div>
    <div class="top-icon"><svg width="30" height="30" viewBox="0 0 30 30"><path d="M15 5c-5 0-7 4-7 8v7l-3 4h20l-3-4v-7c0-4-2-8-7-8z" fill="#fff"/><circle cx="15" cy="26" r="2.5" fill="#fff"/></svg><span class="badge">4</span></div>
  </div>
</header>

<aside class="sidebar">
  <div class="user">
    <div class="avatar"><svg width="70" height="70" viewBox="0 0 70 70"><circle cx="35" cy="28" r="14" fill="#2e90c7"/><path d="M14 70c0-18 9-26 21-26s21 8 21 26z" fill="#2e90c7"/></svg></div>
    <div class="welcome">Welcome back,<b>Dr. Varenko</b></div>
    <div class="logout">Log out</div>
  </div>
  <ul class="menu">
    <li class="active"><svg width="24" height="16" viewBox="0 0 24 16"><path d="M2 15a10 10 0 0 1 20 0z" fill="#fff"/><path d="M12 14l5-8" stroke="#2b8bc3" stroke-width="2.5"/></svg>Dashboard</li>
    <li><svg width="20" height="20" viewBox="0 0 20 20"><circle cx="10" cy="10" r="9.5" fill="#fff"/><circle cx="10" cy="8" r="4" fill="#2e90c7"/><path d="M3.5 16c1-4 4-5 6.5-5s5.5 1 6.5 5z" fill="#2e90c7"/></svg>Patiente</li>
    <li><svg width="22" height="16" viewBox="0 0 22 16"><rect x="1" y="1" width="20" height="14" fill="#fff"/><path d="M1 1l10 8 10-8" fill="none" stroke="#555" stroke-width="1.5"/></svg>Mail</li>
    <li><svg width="20" height="20" viewBox="0 0 20 20"><path d="M1 1v18h18" fill="none" stroke="#fff" stroke-width="2"/><rect x="5" y="12" width="2" height="5" fill="#fff"/><rect x="9" y="9" width="2" height="8" fill="#fff"/><rect x="13" y="6" width="2" height="11" fill="#fff"/><rect x="16" y="3" width="2" height="14" fill="#fff"/></svg>Charts</li>
    <li><svg width="20" height="20" viewBox="0 0 20 20"><path d="M3 17 14 6M6 3l11 11M14 6l3-3M3 17l-1 1" stroke="#fff" stroke-width="3"/></svg>Setting</li>
  </ul>
</aside>

<main class="main">
  <div class="page-head">
    <svg width="56" height="34" viewBox="0 0 56 34"><path d="M3 32a25 25 0 0 1 50 0z" fill="#333"/><path d="M12 30a16 16 0 0 1 32 0z" fill="#e8e8e8"/><path d="M28 31l10-18" stroke="#333" stroke-width="5"/><circle cx="28" cy="31" r="4" fill="#333"/></svg>
    <h1>Dashboard</h1>
  </div>

  <div class="crumbs">
    <div class="crumb-home"><svg width="18" height="16" viewBox="0 0 18 16"><path d="M9 1 1 8h2.5v7h4v-4h3v4h4V8H17z" fill="#fff"/></svg>Home</div>
    <div class="crumb-current">Dashboard</div>
  </div>

  <section class="panel" style="left:26px;top:136px;width:427px;height:131px">
    <div class="panel-head"><span>WEITER</span><span>→</span></div>
    <svg style="position:absolute;left:28px;top:55px" width="34" height="46" viewBox="0 0 34 46"><circle cx="17" cy="12" r="11" fill="#2e90c7"/><path d="M3 46v-11c0-6 5-10 14-10s14 4 14 10v11z" fill="#2e90c7"/></svg>
    <div class="tile-title" style="top:54px"><strong>Profile</strong><span>Profile bearbeiten</span></div>
  </section>

  <section class="panel" style="left:26px;top:285px;width:427px;height:131px">
    <div class="panel-head"><span>ALLE ANSEHEN</span><span>→</span></div>
    <svg style="position:absolute;left:12px;top:43px" width="102" height="68" viewBox="0 0 102 68"><g fill="#2e90c7"><circle cx="15" cy="12" r="11"/><path d="M0 46v-11c0-6 5-10 15-10s15 4 15 10v11z"/><circle cx="84" cy="12" r="11"/><path d="M69 46v-11c0-6 5-10 15-10s15 4 15 10v11z"/><circle cx="50" cy="34" r="11"/><path d="M35 68v-11c0-6 5-10 15-10s15 4 15 10v11z"/></g></svg>
    <div class="tile-title" style="top:54px"><strong>Patienten</strong><span>Patienten verwalten</span></div>
  </section>

  <section class="panel" style="left:503px;top:136px;width:427px;height:217px">
    <div class="panel-head large"><span>Willkomen: Dr. Varenko</span></div>
    <div class="welcome-body">
      <div class="status"><span>Der Status Ihres offentlicen Profils ist derzeit:</span><span class="btn btn-ok">Alles OK</span></div>
      <p>cras non lacus nec dolor suscipit henderit. Interdum et malesuada fames ac ante ipsum primis in faucibus. Praesent fermentum quis purus a vluputate. Duis ultricies a nisl sed vestibulum. Morbi elementum lobortis dolr sed elementum. Nullam a aullamcorper turpis, eu tempus nulla. Duis gravida accumsan erat, at eleifend leo iaculis eu.</p>
    </div>
  </section>

  <section class="panel" style="left:26px;top:441px;width:429px;height:283px">
    <div class="panel-head large"><span>Pie</span></div>
    <svg style="position:absolute;left:62px;top:72px" width="206" height="126" viewBox="-103 -50 206 126" role="img" aria-label="Pie chart of seven series">
      <g>
        <path d="M100 0A100 45 0 0 1 96.6 11.6L96.6 33.6A100 45 0 0 0 100 22Z" fill="#a01418"/>
        <path d="M96.6 11.6A100 45 0 0 1 0 45L0 67A100 45 0 0 0 96.6 33.6Z" fill="#8a7c10"/>
        <path d="M0 45A100 45 0 0 1 -98.5 7.8L-98.5 29.8A100 45 0 0 0 0 67Z" fill="#0b9a0b"/>
        <path d="M-98.5 7.8A100 45 0 0 1 -100 0L-100 22A100 45 0 0 0 -98.5 29.8Z" fill="#8a6a3e"/>
      </g>
      <path d="M0 0L0 -45A100 45 0 0 1 86.6 -22.5Z" fill="#f7941e"/>
      <path d="M0 0L86.6 -22.5A100 45 0 0 1 96.6 11.6Z" fill="#ed1c24"/>
      <path d="M0 0L96.6 11.6A100 45 0 0 1 0 45Z" fill="#f5ec1f"/>
      <path d="M0 0L0 45A100 45 0 0 1 -98.5 7.8Z" fill="#0ef40e"/>
      <path d="M0 0L-98.5 7.8A100 45 0 0 1 -50 -39Z" fill="#c69c6d"/>
      <path d="M0 0L-50 -39A100 45 0 0 1 -20.8 -44Z" fill="#92278f"/>
      <path d="M0 0L-20.8 -44A100 45 0 0 1 0 -45Z" fill="#27aae1"/>
    </svg>
    <ul class="legend">
      <li><i style="background:#f7941e"></i>Series 1</li>
      <li><i style="background:#ed1c24"></i>Series 2</li>
      <li><i style="background:#27aae1"></i>Series 3</li>
      <li><i style="background:#92278f"></i>Series 4</li>
      <li><i style="background:#c69c6d"></i>Series 5</li>
      <li><i style="background:#0ef40e"></i>Series 6</li>
      <li><i style="background:#f5ec1f"></i>Series 7</li>
    </ul>
  </section>

  <section class="panel" style="left:503px;top:441px;width:427px;height:283px">
    <div class="panel-head large"><span>Stat</span></div>
    <div class="search"><div>Search....</div><span><svg width="16" height="16" viewBox="0 0 16 16"><circle cx="6.5" cy="6.5" r="5" fill="none" stroke="#fff" stroke-width="2"/><path d="M10 10l5 5" stroke="#fff" stroke-width="2.5"/></svg></span></div>
    <table class="stat-table">
      <thead><tr><th>Name</th><th>Position</th><th>Start date</th><th>Salary</th></tr></thead>
      <tbody>
        <tr><td>Gerda</td><td>Chefin</td><td>1.11.2013</td><td>Salami</td></tr>
        <tr><td>Gerda</td><td>Chefin</td><td>2.11.2013</td><td>Salami</td></tr>
        <tr><td>Gerda</td><td>Chefin</td><td>3.11.2013</td><td>Salami</td></tr>
        <tr><td>Gerda</td><td>Chefin</td><td>4.11.2013</td><td>Salami</td></tr>
        <tr><td>Gerda</td><td>Chefin</td><td>5.11.2013</td><td>Salami</td></tr>
      </tbody>
    </table>
    <div class="pager-info">Showing 1 to 5 of 8 entries</div>
    <div class="pager"><span class="btn">← Previous</span><span class="btn">1</span><span class="btn">2</span><span class="btn">Next →</span></div>
  </section>
</main>

<footer class="footer">CopyRight © 2014 northlane | All Right Reserved</footer>
</body>
</html>
```